Bref créative |
Web Design: Perk Nuggets | ||
Perk Nuggets | ||
Food | ||
www.perk-nuggets-example.com | ||
Perk Nuggets are an energy packed chocolate truffle that will compete directly against existing energy drink/shot products like Dawn Fuel Shot and Blue Hare. We plan to differentiate ourselves through natural ingredients and a superior taste. Instead of using artificial sweeteners, flavors, and colors to hide the bitterness of the energy blend, the Perk Nugget uses chocolate to deliver a delectable and natural way to get your energy. Each truffle has been hand crafted inline with traditional chocolatier techniques - offering a glossy shell exterior with a rich,creamy ganache center. Our tagline "Bright.Drive" refers to our belief that our product, through taste and natural ingredients, is a smarter way to get the energy you need to be productive. |
Likes: Clean. Professional. No clutter. User-friendly. Unique. Navigation bar with a hover effect. Natural feel. Expresses themes of artisan chocolate, energy, and natural. Dislikes: Clutter. Lack of contrast. Not user friendly. |
Unique/Creative Clean/Simple Professional Exciting Sophisticated Nature |
Soft Orange: C-10 M-53 Y-76 K-1 | ||
Brown: C-37 M-60 Y-100 K-28 | ||
Dark Brown: C-49 M-60 Y-85 K-47 | ||
left side | ||
www.dawnfuelshot-example.com | ||
dawnfuelshot-example.com has a nice layout and is user-friendly. Looking for a feel like the logo that won this previous project: http://orders.markcraftplace-example.com/drafts/display/contest/740163/draft/5531904 Other colors used in logo: Beige C-4 M-14 Y-30 K-0 Dark Beige: C-17 M-30 Y-57 K-0 Vibrant Orange C-0 M-33 Y-70 K-0 Fonts in logo: Bauhaus(Medium) Eurostile(Regular) Openhouse I'm okay with Nav placement on top (below header) and on the left side. Just depends how it flows into the rest of the design. Font isn't really important. easy to change. Top images: unique, simple and professional that conveys an innovative and exciting product. |

```html
<!DOCTYPE html>
<html lang="en">
<head>
<meta charset="utf-8">
<title>Perk Nuggets – Natural Energy Truffles</title>
<link rel="stylesheet" href="https://fonts.googleapis.com/css2?family=Questrial&family=Arimo:wght@400;700&display=swap">
<style>
  :root {
    --page-bg: #e6e6e6;
    --page-bg-light: #f7f7f7;
    --panel-white: #ffffff;
    --band-orange: #dc8a4f;
    --nav-brown: #c2733a;
    --nav-active: #e99a44;
    --heading-orange: #c26c2b;
    --brand-brown: #6b4423;
    --text-dark: #3a3a3a;
    --text-white: #ffffff;
    --button-orange: #f0a04b;
    --button-border: #b86a2c;
    --rule-grey: #d6d6d6;
    --footer-text: #8a6a50;
  }
  * { box-sizing: border-box; margin: 0; padding: 0; }
  html, body { width: 1200px; height: 814px; overflow: hidden; }
  body {
    position: relative;
    background: radial-gradient(ellipse at 50% 30%, var(--page-bg-light) 0%, var(--page-bg) 70%);
    font-family: "Arimo", Arial, sans-serif;
    color: var(--text-dark);
  }
  .brand {
    position: absolute; left: 0; width: 1200px; top: 70px;
    display: flex; justify-content: center; align-items: center; gap: 14px;
  }
  .brand-dot { width: 34px; height: 34px; border-radius: 50%; background: var(--band-orange); }
  .brand-name {
    font-family: "Questrial", sans-serif; font-size: 54px; color: var(--brand-brown);
  }
  .social { position: absolute; top: 142px; left: 868px; display: flex; gap: 8px; }
  .social-badge { width: 36px; height: 36px; border-radius: 4px; background: #8a8a8a; }
  .social-badge:nth-child(2) { background: #4a68a8; }
  .social-badge:nth-child(3) { background: #58b4e0; }

  .panel { position: absolute; left: 175px; top: 185px; width: 862px; height: 597px; background: var(--panel-white); }
  .feature-band { position: absolute; left: 0; top: 0; width: 862px; height: 276px; background: var(--band-orange); }
  .main-nav { position: absolute; left: 0; top: 0; width: 202px; height: 276px; background: var(--nav-brown); padding-top: 28px; }
  .main-nav a {
    display: block; height: 34px; margin: 0 10px 4px 10px; padding-left: 10px;
    font-family: "Questrial", sans-serif; font-size: 21px; line-height: 34px;
    color: var(--text-white); text-decoration: none;
  }
  .main-nav a.active, .main-nav a:hover { background: var(--nav-active); border: 1px solid #f6c48f; }
  .feature-title {
    position: absolute; left: 216px; top: 14px;
    font-family: "Questrial", sans-serif; font-size: 26px; font-weight: 400; color: var(--text-white);
  }
  .feature-photo { position: absolute; left: 216px; top: 50px; width: 166px; height: 202px; background: linear-gradient(135deg, #f2eee8, #cfc6bb); }
  .feature-copy {
    position: absolute; left: 400px; top: 60px; width: 278px;
    font-size: 13.5px; line-height: 17px; color: var(--text-white); text-indent: 18px;
  }
  .truffle-photo {
    position: absolute; left: 680px; top: 48px; width: 144px; height: 198px; border-radius: 10px;
    background: radial-gradient(circle at 50% 55%, #4a2c1c 0%, #7d563c 38%, #e9d4c3 70%, #f4e6da 100%);
  }

  .section-title {
    position: absolute; left: 29px; top: 292px;
    font-family: "Questrial", sans-serif; font-size: 22px; font-weight: 400; color: var(--heading-orange);
  }
  .section-rule { position: absolute; left: 29px; top: 322px; width: 800px; border-top: 1px solid var(--rule-grey); }
  .photo-strip { position: absolute; left: 29px; top: 329px; width: 797px; height: 86px; display: flex; }
  .strip-photo { flex: 1; }
  .strip-photo.library { background: linear-gradient(135deg, #8fa3b8, #d8c7a8); }
  .strip-photo.office { background: linear-gradient(135deg, #c9ced6, #6d7a8a); }
  .strip-photo.runner { background: linear-gradient(135deg, #e8eef3, #9aa8b5); }
  .strip-photo.hand { background: linear-gradient(135deg, #3c3f48, #a7acb5); }
  .strip-photo.lights { background: linear-gradient(135deg, #1d1a24, #b8742e, #2a2030); }
  .body-copy { position: absolute; top: 439px; width: 380px; font-size: 13.5px; line-height: 16px; color: var(--text-dark); }
  .body-copy.left { left: 29px; }
  .body-copy.right { left: 468px; width: 352px; }
  .order-button {
    position: absolute; left: 509px; top: 540px; width: 175px; height: 32px;
    background: var(--button-orange); border: 2px solid var(--button-border); border-radius: 3px;
    font-family: "Questrial", sans-serif; font-size: 18px; color: var(--brand-brown);
    display: flex; align-items: center; justify-content: center; font-weight: 700;
  }
  .site-footer {
    position: absolute; left: 175px; top: 786px; width: 862px; height: 22px;
    border-top: 1px solid var(--rule-grey);
    display: flex; justify-content: space-between; align-items: center;
    font-size: 10.5px; color: var(--footer-text);
  }
  .footer-links { display: flex; gap: 6px; }
  .footer-links a { color: var(--footer-text); text-decoration: none; }
</style>
</head>
<body>
  <header class="brand">
    <span class="brand-dot"></span>
    <span class="brand-name">Perk Nuggets</span>
  </header>
  <div class="social">
    <span class="social-badge"></span>
    <span class="social-badge"></span>
    <span class="social-badge"></span>
  </div>

  <main class="panel">
    <section class="feature-band">
      <nav class="main-nav">
        <a class="active" href="#">Home</a>
        <a href="#">About Us</a>
        <a href="#">Products</a>
        <a href="#">News</a>
        <a href="#">Contact Us</a>
      </nav>
      <h1 class="feature-title">Natural ingredients and a superior taste</h1>
      <div class="feature-photo" role="img" aria-label="Photo of a student studying with books and a mug"></div>
      <p class="feature-copy">Instead of using artificial sweeteners, flavors, and colors to hide the bitterness of the energy blend, the Perk Nugget uses chocolate to deliver a delectable and natural way to get your energy. Each truffle has been hand crafted inline with traditional chocolatier techniques - offering a glossy shell exterior with a rich,creamy ganache center.</p>
      <div class="truffle-photo" role="img" aria-label="Photo of two glossy chocolate truffles"></div>
    </section>

    <h2 class="section-title">Perk Nuggets: Bright Drive</h2>
    <div class="section-rule"></div>
    <div class="photo-strip">
      <div class="strip-photo library" role="img" aria-label="Photo of a person reading in a library"></div>
      <div class="strip-photo office" role="img" aria-label="Photo of an office worker at a desk"></div>
      <div class="strip-photo runner" role="img" aria-label="Photo of a runner on a bright track"></div>
      <div class="strip-photo hand" role="img" aria-label="Photo of a hand reaching towards light"></div>
      <div class="strip-photo lights" role="img" aria-label="Photo of city light trails at night"></div>
    </div>
    <p class="body-copy left">Lorem ipsum dolor sit amet, consectetur adipiscing elit. Praesent a arcu eget odio rhoncus placerat. Nullam ullamcorper, elit sit amet scelerisque tempus, tellus nunc ultrices risus, nec euismod urna orci ac magna. Morbi venenatis viverra mauris, nec malesuada dolor congue in. In ut bibendum ipsum. Cras nisl justo, vestibulum id suscipit sed, tincidunt vitae sapien.</p>
    <p class="body-copy right">Donec turpis enim, elementum non elementum ut, ullamcorper ut diam. Sed nec velit vel leo lobortis scelerisque. Fusce auctor rhoncus magna, sit amet molestie libero tincidunt a. Pellentesque pharetra massa non ligula scelerisque semper imperdiet nibh sodales.</p>
    <a class="order-button" href="#">Order some now!</a>
  </main>

  <footer class="site-footer">
    <span>Copyright Perk Nuggets 2012</span>
    <span class="footer-links">
      <a href="#">Home</a>·<a href="#">About Us</a>·<a href="#">Products</a>·<a href="#">News</a>·<a href="#">Contact Us</a>·<a href="#">Privacy Policy</a>·<a href="#">Site Map</a>
    </span>
  </footer>
</body>
</html>
```